Heating and Cooling Company mobile website

We need a website specifically designed for a viewing on a mobile device.

We serve the northern New Jersey heating, cooling and electrical residential market.

The goal is the drive traffic to the site by using Brindle Pay Per click. People will be searching for an HVAC contractor, and they land on our page. They need to get key info quickly without all the clutter of a desktop type of site.

Target Market(s)

Homeowners

Industry/Entity Type

Hvac

Coding

Coded - Design and coding required

Number of Pages Required

5+ page

Font styles to use
Serif

Requirements
Must have
• View attachments to see samples of the desktop version. It must have a similar color scheme
• The copy of the website is also attached
Nice to have
• Would like it to have a sort of Talvix feel to it. Make it seem like its an app that people are using and that its exciting to be on the website. It would be nice to have a page where customers can book appointments

```html
<!DOCTYPE html>
<html lang="en">
<head>
<meta charset="utf-8">
<title>Hearthway Specialists – Mobile Screens</title>
<link href="https://fonts.googleapis.com/css2?family=Oswald:wght@400;500;600&family=Roboto+Condensed:wght@300;400;700&display=swap" rel="stylesheet">
<style>
:root{
  --red:#a3232f;
  --red-soft:#c4545d;
  --navy:#3b4566;
  --cream:#f1e8d4;
  --ribbon:#e3ded0;
  --orange:#e8871e;
  --teal:#4f8fa0;
  --tile:#e6e6e6;
  --tile-alt:#dcdcdc;
  --ink:#555;
  --charcoal:#2f2f2f;
  --frame:#2b2b2b;
  --page:#f3f3f3;
}
*{box-sizing:border-box;margin:0;padding:0}
html,body{width:1200px;height:894px;overflow:hidden;background:var(--page)}
body{font-family:"Roboto Condensed",Arial,sans-serif;color:var(--ink)}
.board{display:grid;grid-template-columns:repeat(5,205px);grid-template-rows:repeat(2,360px);column-gap:29px;row-gap:58px;padding:58px 29px}
.screen{position:relative;width:205px;height:360px;border:2px solid var(--frame);background:#fff;overflow:hidden}

/* shared header */
.schedule-bar{height:46px;background:var(--red);display:flex;align-items:center;padding:0 10px;gap:9px;color:#fff;font-family:Oswald,sans-serif;font-weight:500;font-size:11px;letter-spacing:.2px}
.schedule-bar .label{flex:1}
.ribbon{margin:18px auto 14px;width:172px;height:24px;background:var(--ribbon);clip-path:polygon(0 0,100% 0,94% 50%,100% 100%,0 100%,6% 50%);display:flex;align-items:center;justify-content:center;font-family:Oswald,sans-serif;font-weight:500;font-size:10.5px;color:var(--red)}
.list{list-style:none;padding:0 8px 0 12px}
.list li{position:relative;padding-left:20px;font-size:7.4px;font-weight:400;line-height:14px;color:var(--ink)}
.list li::before{content:"";position:absolute;left:0;top:3px;width:8px;height:8px;border-radius:50%;background:var(--orange)}

/* screen 1 */
.home{background:var(--cream)}
.home-top{height:52px;background:var(--navy);display:flex;align-items:flex-start;justify-content:space-between;padding:6px 6px 0}
.call{display:flex;gap:3px;align-items:center;color:#fff;font-family:Oswald,sans-serif;font-size:8.5px;line-height:9px;font-weight:500}
.brand-home{position:absolute;left:50%;top:14px;transform:translateX(-50%);background:var(--red);color:var(--cream);font-family:Oswald,sans-serif;font-weight:500;font-size:13px;padding:10px 12px;text-align:center;line-height:14px;width:112px}
.burger{display:flex;flex-direction:column;gap:3px;margin-top:5px}
.burger span{display:block;width:20px;height:2px;background:#fff}
.tagline{margin:46px 12px 0;border-top:2px solid var(--teal);border-bottom:2px solid var(--teal);padding:7px 2px;text-align:center;font-family:Oswald,sans-serif;font-weight:500;font-size:9.5px;line-height:11px;color:var(--navy)}
.hero{margin-top:5px;height:148px;background:linear-gradient(160deg,#e9e4da 0%,#cfc3b0 45%,#a69a8a 100%);position:relative}
.read-more{position:absolute;left:58px;bottom:8px;background:var(--red);border:1px solid var(--orange);color:#fff;font-size:6.5px;padding:4px 6px;font-family:Oswald,sans-serif}
.hours{position:absolute;left:0;right:0;bottom:0;height:44px;background:var(--navy);display:flex;align-items:center;padding:0 6px;gap:8px;color:#fff}
.open{display:flex;flex-direction:column;font-size:6px;line-height:8px;flex:none}
.open .time{font-family:Oswald,sans-serif;font-size:10.5px;line-height:12px;border-bottom:1px solid #fff;padding-bottom:1px;margin-bottom:2px}
.open b{font-family:Oswald,sans-serif;font-size:9px;line-height:10px;letter-spacing:4px;font-weight:500}
.hours p{font-size:5.4px;line-height:6.5px;font-style:italic;text-align:center;flex:1}

/* screen 2 */
.services-grid{display:grid;grid-template-columns:1fr 1fr;grid-template-rows:1fr 1fr;height:100%}
.tile{background:var(--tile);display:flex;flex-direction:column;align-items:center;justify-content:flex-end;padding-bottom:18px;gap:14px;color:var(--red);font-family:Oswald,sans-serif;font-weight:500;font-size:9.5px;text-align:center;line-height:11px}
.tile.alt{background:var(--tile-alt)}
.tile-art{width:62px;height:62px;border-radius:8px;background:linear-gradient(160deg,var(--red-soft),var(--red))}

/* screen 8 */
.testimonial{background:var(--cream);text-align:center}
.speak{margin:16px auto 0;width:170px;height:24px;background:var(--red);clip-path:polygon(0 0,100% 0,95% 50%,100% 100%,0 100%,5% 50%);color:#fff;font-family:Oswald,sans-serif;font-weight:500;font-size:10.5px;line-height:24px}
.avatar{width:98px;height:98px;border-radius:50%;border:3px solid var(--orange);margin:12px auto 0;background:radial-gradient(circle at 50% 40%,#cfa88a,#8a6a55 70%,#5b4a40)}
.quote-mark{font-family:Oswald,sans-serif;font-size:34px;color:#c9c2b4;line-height:30px;margin-top:10px}
.testimonial p{font-size:8px;line-height:15px;color:#6a6358;padding:4px 10px 0}
.dots{display:flex;justify-content:center;gap:3px;margin-top:40px}
.dots span{width:9px;height:9px;border-radius:50%;background:#c5c5c5}
.dots span.on{background:var(--red)}

/* screens 9 & 10 */
.footer-screen{background:var(--navy);color:#fff}
.brand-strip{height:50px;background:#fff;display:flex;justify-content:center}
.brand-chip{background:var(--red);color:var(--cream);font-family:Oswald,sans-serif;font-weight:500;font-size:10px;line-height:11px;text-align:center;padding:8px;width:82px;height:54px;position:relative;top:8px}
.contact{text-align:center;font-size:7.2px;line-height:14px;padding:22px 6px 6px;border-bottom:1px solid #56607f;margin:0 6px}
.follow{text-align:center;font-family:Oswald,sans-serif;font-size:7.5px;color:var(--orange);padding-top:7px}
.social{display:flex;justify-content:center;gap:6px;margin:6px 0 12px}
.social span{width:16px;height:16px;border-radius:50%;background:#fff;border:2px solid var(--orange)}
.link-cols{display:grid;grid-template-columns:1fr 1fr;padding:10px 7px 0;border-top:1px solid #56607f;font-size:7.2px;line-height:14px}
.link-cols ul{list-style:none}
.link-cols .head{color:var(--orange);font-weight:700}
.copyright{background:var(--charcoal);text-align:center;font-size:7.2px;line-height:14px;padding:10px 6px;margin-top:14px}
.footer-screen.short .link-cols{border-top:none;padding-top:26px}
</style>
</head>
<body>
<main class="board">

  <!-- 1 Home -->
  <section class="screen home">
    <div class="home-top">
      <div class="call">
        <svg width="11" height="14" viewBox="0 0 11 14"><path d="M3 1 L5 4 L3.5 5.5 Q4.5 8.5 6.5 10 L8 8.5 L10.5 10.5 L9 13 Q2 11 1 2 Z" fill="#fff"/></svg>
        <span>CALL<br>NOW</span>
      </div>
      <div class="burger"><span></span><span></span><span></span></div>
    </div>
    <div class="brand-home">HEARTHWAY<br>SPECIALISTS</div>
    <h1 class="tagline">THE BEST WAY TO LIVE IN NEW<br>JERSEY IS WITH COMFORT!</h1>
    <div class="hero" role="img" aria-label="Family photo of parents and two children relaxing at home">
      <span class="read-more">READ MORE ›</span>
    </div>
    <div class="hours">
      <div class="open"><span class="time">11:30AM</span><span>YES WE ARE</span><b>OPEN</b></div>
      <p>SERIOUSLY, DON'T BE AFRAID TO CALL AT ANY TIME WE LIVE FOR THIS. JUST GIVE US A MIN TO GET SOME COFFEE ON THE WAY OVER</p>
    </div>
  </section>

  <!-- 2 Services menu -->
  <section class="screen">
    <div class="services-grid">
      <div class="tile"><div class="tile-art" role="img" aria-label="Flame illustration for heating"></div>HEATING</div>
      <div class="tile alt"><div class="tile-art" role="img" aria-label="Air conditioner unit illustration"></div>AIR<br>CONDITIONING</div>
      <div class="tile alt"><div class="tile-art" role="img" aria-label="Electrical plug illustration"></div>ELECTRICAL</div>
      <div class="tile"><div class="tile-art" role="img" aria-label="Ventilation grille illustration"></div>VENTILATION</div>
    </div>
  </section>

  <!-- 3 Services we offer -->
  <section class="screen">
    <header class="schedule-bar">
      <svg width="18" height="16" viewBox="0 0 18 16"><rect x="1" y="2" width="16" height="13" rx="1" fill="none" stroke="var(--orange)" stroke-width="1.6"/><rect x="1" y="2" width="16" height="3" fill="var(--orange)"/><g fill="var(--orange)"><rect x="4" y="7" width="2.5" height="2"/><rect x="8" y="7" width="2.5" height="2"/><rect x="12" y="7" width="2.5" height="2"/><rect x="4" y="11" width="2.5" height="2"/><rect x="8" y="11" width="2.5" height="2"/></g></svg>
      <span class="label">SCHEDULE A SERVICE</span>
      <svg width="11" height="11" viewBox="0 0 11 11"><circle cx="5.5" cy="5.5" r="5.5" fill="#fff"/><path d="M3 5.5 H7.5 M5.5 3.3 L7.8 5.5 L5.5 7.7" stroke="var(--red)" stroke-width="1.5" fill="none"/></svg>
    </header>
    <h2 class="ribbon">THE SERVICES WE OFFER</h2>
    <ul class="list">
      <li>We solve heating, air conditioning and electrical problems.</li>
      <li>We Install heating and cooling equipment</li>
      <li>We work 24-7</li>
      <li>We come prepared for any job, trucks are oversized and well stocked.</li>
      <li>It is very rare that we cannot get a system working. If you call us it wont result in time or money wasted and the system still not working</li>
      <li>We offer tune up services</li>
      <li>We offer maintanance plans</li>
    </ul>
  </section>

  <!-- 4 Problems we fix -->
  <section class="screen">
    <header class="schedule-bar">
      <svg width="18" height="16" viewBox="0 0 18 16"><rect x="1" y="2" width="16" height="13" rx="1" fill="none" stroke="var(--orange)" stroke-width="1.6"/><rect x="1" y="2" width="16" height="3" fill="var(--orange)"/><g fill="var(--orange)"><rect x="4" y="7" width="2.5" height="2"/><rect x="8" y="7" width="2.5" height="2"/><rect x="12" y="7" width="2.5" height="2"/><rect x="4" y="11" width="2.5" height="2"/><rect x="8" y="11" width="2.5" height="2"/></g></svg>
      <span class="label">SCHEDULE A SERVICE</span>
      <svg width="11" height="11" viewBox="0 0 11 11"><circle cx="5.5" cy="5.5" r="5.5" fill="#fff"/><path d="M3 5.5 H7.5 M5.5 3.3 L7.8 5.5 L5.5 7.7" stroke="var(--red)" stroke-width="1.5" fill="none"/></svg>
    </header>
    <h2 class="ribbon">PROBLEM WE FIX</h2>
    <ul class="list">
      <li>No heat</li>
      <li>No cooling</li>
      <li>Weird noises</li>
      <li>Weird smells, burning smells, gas smells, smoke smells, oil smells.</li>
      <li>Runs but no heat</li>
      <li>Runs but no air conditioning</li>
      <li>Soot; soot on the unit, soot blowing out of the unit, soot here, soot there. We've seen it before and cleaned it up.</li>
      <li>Water leaking</li>
      <li>Needs freon</li>
      <li>Unit ices up</li>
      <li>Unit shakes</li>
    </ul>
  </section>

  <!-- 5 Problems we fix (cont.) -->
  <section class="screen">
    <header class="schedule-bar">
      <svg width="18" height="16" viewBox="0 0 18 16"><rect x="1" y="2" width="16" height="13" rx="1" fill="none" stroke="var(--orange)" stroke-width="1.6"/><rect x="1" y="2" width="16" height="3" fill="var(--orange)"/><g fill="var(--orange)"><rect x="4" y="7" width="2.5" height="2"/><rect x="8" y="7" width="2.5" height="2"/><rect x="12" y="7" width="2.5" height="2"/><rect x="4" y="11" width="2.5" height="2"/><rect x="8" y="11" width="2.5" height="2"/></g></svg>
      <span class="label">SCHEDULE A SERVICE</span>
      <svg width="11" height="11" viewBox="0 0 11 11"><circle cx="5.5" cy="5.5" r="5.5" fill="#fff"/><path d="M3 5.5 H7.5 M5.5 3.3 L7.8 5.5 L5.5 7.7" stroke="var(--red)" stroke-width="1.5" fill="none"/></svg>
    </header>
    <h2 class="ribbon">PROBLEM WE FIX</h2>
    <ul class="list">
      <li>Flame drops out</li>
      <li>Lights on unit flashing</li>
      <li>No hot water</li>
      <li>Breaker trips</li>
      <li>Lights dim</li>
      <li>Lack of air flow</li>
      <li>Heating or cooling costs too high</li>
      <li>Continual problems, no one was able ti fix it</li>
      <li>2nd opinion</li>
      <li>Thermostat problems</li>
      <li>Spouse complaining about something, HVAC related.</li>
      <li>C.O alarms going off</li>
      <li>Inspector issues</li>
    </ul>
  </section>

  <!-- 6 Why call us -->
  <section class="screen">
    <header class="schedule-bar">
      <svg width="18" height="16" viewBox="0 0 18 16"><rect x="1" y="2" width="16" height="13" rx="1" fill="none" stroke="var(--orange)" stroke-width="1.6"/><rect x="1" y="2" width="16" height="3" fill="var(--orange)"/><g fill="var(--orange)"><rect x="4" y="7" width="2.5" height="2"/><rect x="8" y="7" width="2.5" height="2"/><rect x="12" y="7" width="2.5" height="2"/><rect x="4" y="11" width="2.5" height="2"/><rect x="8" y="11" width="2.5" height="2"/></g></svg>
      <span class="label">SCHEDULE A SERVICE</span>
      <svg width="11" height="11" viewBox="0 0 11 11"><circle cx="5.5" cy="5.5" r="5.5" fill="#fff"/><path d="M3 5.5 H7.5 M5.5 3.3 L7.8 5.5 L5.5 7.7" stroke="var(--red)" stroke-width="1.5" fill="none"/></svg>
    </header>
    <h2 class="ribbon">WHY CALL US</h2>
    <ul class="list">
      <li>We invest into tools and training. Finding problems quickly and accurately helps us keep costs to the consumer low</li>
      <li>We like to fix things and solve problems. We have an HVAC hero complex.</li>
      <li>We use trucks that are well stocked and large. We modified several fire rescue trucks so we can carry more tools and supplies than any normal van can carry. The chances are that we have the parts we need to get a break down fixed.</li>
      <li>We use technology that tracks what the most common parts are and we make sure to stock those parts.</li>
    </ul>
  </section>

  <!-- 7 Why call us (cont.) -->
  <section class="screen">
    <header class="schedule-bar">
      <svg width="18" height="16" viewBox="0 0 18 16"><rect x="1" y="2" width="16" height="13" rx="1" fill="none" stroke="var(--orange)" stroke-width="1.6"/><rect x="1" y="2" width="16" height="3" fill="var(--orange)"/><g fill="var(--orange)"><rect x="4" y="7" width="2.5" height="2"/><rect x="8" y="7" width="2.5" height="2"/><rect x="12" y="7" width="2.5" height="2"/><rect x="4" y="11" width="2.5" height="2"/><rect x="8" y="11" width="2.5" height="2"/></g></svg>
      <span class="label">SCHEDULE A SERVICE</span>
      <svg width="11" height="11" viewBox="0 0 11 11"><circle cx="5.5" cy="5.5" r="5.5" fill="#fff"/><path d="M3 5.5 H7.5 M5.5 3.3 L7.8 5.5 L5.5 7.7" stroke="var(--red)" stroke-width="1.5" fill="none"/></svg>
    </header>
    <h2 class="ribbon">WHY CALL US</h2>
    <ul class="list">
      <li>We respect your house.</li>
      <li>We respect your time and we will not waste it.</li>
      <li>We use clear language to tell you what issues we find when we perform a service call.</li>
      <li>Our word is our bond</li>
      <li>We actually do service work. We are not using a service call as some sort of high pressure sales tactic to sell new HVAC system.</li>
      <li>We will show you all of our findings. No trickery or slight of hand. You will under stand our work process.</li>
    </ul>
  </section>

  <!-- 8 Client speak -->
  <section class="screen testimonial">
    <h2 class="speak">CLIENT SPEAK</h2>
    <div class="avatar" role="img" aria-label="Portrait photo of a client"></div>
    <div class="quote-mark">”</div>
    <p>Suspendisse eu tincidunt libero. Phasellus nec arcu euismod augue varius sagittis. Nullam eget mollis risus, nec aliquam dui.</p>
    <div class="dots"><span></span><span></span><span></span><span class="on"></span><span></span><span></span></div>
  </section>

  <!-- 9 Contact footer -->
  <section class="screen footer-screen">
    <div class="brand-strip"><div class="brand-chip">HEARTHWAY<br>SPECIALISTS</div></div>
    <div class="contact">
      P.O Box 418<br>Fernbrook NJ 07099<br>New Jersey Electrical License Number 20451<br>NJ Home Improvement Contractors License<br>Number 13VH0918342
    </div>
    <div class="follow">FOLLOW US ON</div>
    <div class="social"><span></span><span></span><span></span></div>
    <nav class="link-cols">
      <ul><li>Home</li><li>About</li><li>Services</li><li>Testimonials</li><li>Blog</li><li>Contact</li></ul>
      <ul><li class="head">Heating</li><li>New Installation</li><li>Repair &amp; Service</li><li>Heat Pumps</li><li>Boilers</li><li>Radiant Heat Systems</li></ul>
    </nav>
  </section>

  <!-- 10 Services footer -->
  <section class="screen footer-screen short">
    <div class="brand-strip"><div class="brand-chip">HEARTHWAY<br>SPECIALISTS</div></div>
    <nav class="link-cols">
      <ul><li class="head">AIR CONDITIONING</li><li>New Installation</li><li>Repair &amp; Service</li><li>Ductless Syatems</li></ul>
      <ul><li class="head">OTHER SERVICES</li><li>Indoor Air Quality</li><li>Thermoststs &amp; Zoning</li><li>Generators</li><li>Products</li></ul>
    </nav>
    <div class="copyright">2017 Hearthway Heating &amp; Cooling.<br>All Rights Reserved.</div>
  </section>

</main>
</body>
</html>
```